Business Card design for a mini spa

business card for a small natural skincare/waxing spa. I need a modern, clean, classy card that draws people in but also need to be able to write future appointments on one side of it.

Target Market(s)

women age 16-70

Industry/Entity Type

Beauty Salon

Contact Information for Business Card

Fernlight Skin Care 907-318-2796
2958 W Talvenby Halvern, AK 99571
Facial, Waxing, Spray Tanning,

Colors
33b8a4

Requirements
Must have
• Fernlight logo with flower
• my tag line "quiet roots bright bloom"
• 907-318-2796
• 2958 W Talvenby
• a place to write ......Your Next Appointment
• Mira Oskenfeld
Nice to have
• something modern, elegant, clean and simple with my attached logo. I also attached a few pictures of what I like along with a color pallet and a few fonts that I like.
Should not have
• no pictures of people in a spa I do not want your typical spa pictures like stone, people receiving a treatment.

```html
<!DOCTYPE html>
<html lang="en">
<head>
<meta charset="utf-8">
<title>Fernlight Skin Care – Business Card</title>
<link rel="stylesheet" href="https://fonts.googleapis.com/css2?family=Josefin+Sans:wght@300&family=Mulish:wght@400&family=Courgette&display=swap">
<style>
  :root {
    --backdrop: #000000;
    --teal: #6ecbc6;
    --teal-line: #72cdc8;
    --gold: #c6ad84;
    --front-edge: #c9e9e6;
    --front-center: #e6f5f3;
    --back-base: #ffffff;
    --pattern-tint: #eef7f6;
    --pattern-warm: #f6f1ea;
  }
  * { box-sizing: border-box; margin: 0; padding: 0; }
  html, body {
    width: 1200px; height: 1000px; overflow: hidden;
    background: var(--backdrop);
  }
  .canvas { position: relative; width: 1200px; height: 1000px; }

  .card {
    position: absolute; left: 258px; width: 683px; height: 390px; overflow: hidden;
  }

  /* Front */
  .card--front {
    top: 102px;
    background: radial-gradient(ellipse 60% 65% at 50% 42%, var(--front-center) 0%, var(--front-edge) 100%);
  }
  .front-wordmark {
    position: absolute; left: 0; right: 0; top: 106px;
    text-align: center;
    font-family: "Josefin Sans", sans-serif; font-weight: 300;
    font-size: 74px; letter-spacing: 6px; line-height: 1;
    color: var(--gold);
  }
  .front-subline {
    position: absolute; left: 129px; width: 416px; top: 220px;
    display: flex; align-items: center; justify-content: space-between;
  }
  .front-subline .rule { width: 68px; height: 2px; background: var(--teal-line); }
  .front-subline .label {
    font-family: "Josefin Sans", sans-serif; font-weight: 300;
    font-size: 40px; letter-spacing: 3px; line-height: 1; padding-top: 6px;
    color: var(--teal);
  }
  .front-tagline {
    position: absolute; left: 0; right: 0; top: 274px;
    text-align: center;
    font-family: "Courgette", cursive; font-size: 35px; letter-spacing: 1px;
    line-height: 1.2;
    color: var(--gold);
  }

  /* Back */
  .card--back { top: 521px; background: var(--back-base); }
  .back-pattern {
    position: absolute; inset: 0;
    background:
      radial-gradient(circle at 12% 45%, var(--pattern-tint) 0 22%, transparent 40%),
      radial-gradient(circle at 50% 50%, var(--pattern-tint) 0 20%, transparent 42%),
      radial-gradient(circle at 88% 35%, var(--pattern-tint) 0 20%, transparent 40%),
      radial-gradient(circle at 85% 92%, var(--pattern-warm) 0 6%, transparent 14%),
      var(--back-base);
  }
  .back-brand { position: absolute; left: 32px; top: 118px; width: 284px; text-align: center; }
  .back-wordmark {
    font-family: "Josefin Sans", sans-serif; font-weight: 300;
    font-size: 46px; letter-spacing: 3px; line-height: 1;
    color: var(--teal);
  }
  .back-subline {
    margin-top: 20px;
    font-family: "Josefin Sans", sans-serif; font-weight: 300;
    font-size: 30px; letter-spacing: 1px; line-height: 1;
    color: var(--gold);
  }
  .divider {
    position: absolute; left: 341px; top: 69px; width: 2px; height: 171px;
    background: var(--gold);
  }
  .contact {
    position: absolute; left: 373px; top: 76px;
    font-family: "Mulish", sans-serif; font-weight: 400; letter-spacing: 1px;
  }
  .contact-name { font-size: 29px; color: var(--gold); line-height: 1.2; }
  .contact-phone { margin-top: 18px; font-size: 26px; color: var(--teal); line-height: 1.2; }
  .contact-address { margin-top: 8px; font-size: 26px; color: var(--teal); line-height: 28px; }

  .appointment {
    position: absolute; left: 34px; top: 292px;
    font-family: "Mulish", sans-serif; font-size: 20px; color: var(--teal);
    letter-spacing: 0.2px; line-height: 1;
  }
  .write-line {
    position: absolute; height: 0;
    border-top: 2px dotted var(--gold);
  }
  .write-line--first { left: 262px; width: 386px; top: 307px; }
  .write-line--second { left: 36px; width: 612px; top: 356px; }
</style>
</head>
<body>
<div class="canvas">

  <section class="card card--front">
    <div class="front-wordmark">FERNLIGHT</div>
    <div class="front-subline">
      <span class="rule"></span>
      <span class="label">SKIN CARE</span>
      <span class="rule"></span>
    </div>
    <p class="front-tagline">quiet roots bright bloom</p>
  </section>

  <section class="card card--back">
    <div class="back-pattern" role="img" aria-label="Faint repeating pale teal flower pattern background"></div>
    <div class="back-brand">
      <div class="back-wordmark">FERNLIGHT</div>
      <div class="back-subline">SKIN CARE</div>
    </div>
    <div class="divider"></div>
    <div class="contact">
      <p class="contact-name">Mira Oskenfeld</p>
      <p class="contact-phone">907-318-2796</p>
      <p class="contact-address">2958 W Talvenby<br>Halvern, AK 99571</p>
    </div>
    <p class="appointment">NEXT APPOINTMENT</p>
    <div class="write-line write-line--first"></div>
    <div class="write-line write-line--second"></div>
  </section>

</div>
</body>
</html>
```